GlowRun Fundraiser

I am looking for a fresh design for the 10th annual GlowRun fundraiser. Green and blue colors need to be incorporated . I attached the current flyer. I would like this flyer for September 20, 2020. This is a fundraiser to help find a cure for NF, nuerofibromatosis.
Updates

We are looking for a fresh look for the 10th annual event

Target Market(s)

Families and individuals of surrounding areas

Colors
0255a3
add136

Requirements
Must have
• Blue and green colors. It is the 10th annual. The logos of RQ CENTER and children’s hospital logo that are shown on the previous flyer I attached
Nice to have
• Eye catching

```html
<!DOCTYPE html>
<html lang="en">
<head>
<meta charset="utf-8">
<title>GlowRun Fundraiser Flyer</title>
<link href="https://fonts.googleapis.com/css2?family=Montserrat:wght@600;800;900&family=Open+Sans:wght@400;600&display=swap" rel="stylesheet">
<style>
  :root{
    --blue:#0255a3;
    --navy:#1d3e8c;
    --green:#add136;
    --ink:#222;
    --white:#fff;
    --stage:#d9d9d9;
  }
  *{box-sizing:border-box;margin:0;padding:0}
  html,body{width:1200px;height:1200px;overflow:hidden;background:var(--stage)}
  .flyer{position:absolute;left:197px;top:30px;width:806px;height:1140px;background:var(--white);overflow:hidden;font-family:"Open Sans",sans-serif;color:var(--ink)}
  .brand{text-align:center;padding-top:46px}
  .brand-name{font-family:"Montserrat",sans-serif;font-weight:800;font-size:58px;color:var(--navy);letter-spacing:1px}
  .brand-name .accent{color:var(--green)}
  .date-bar{position:absolute;left:120px;top:150px;width:600px;height:50px;background:var(--blue);color:var(--white);font-family:"Montserrat",sans-serif;font-weight:800;font-size:26px;display:flex;align-items:center;justify-content:center;gap:18px;z-index:2}
  .date-bar .label{font-weight:600;font-size:20px}
  .date-bar .divider{width:2px;height:32px;background:var(--white)}
  .annual-band{position:absolute;left:0;top:176px;width:100%;height:92px;background:var(--green);display:flex;align-items:flex-end;justify-content:center;padding-bottom:12px}
  .annual-band h1{font-family:"Montserrat",sans-serif;font-weight:900;font-size:44px;color:var(--navy);letter-spacing:1px}
  .highlights{position:absolute;left:0;top:268px;width:100%;height:74px;background:var(--blue);color:var(--white);display:flex;align-items:center;justify-content:center;gap:20px;font-family:"Montserrat",sans-serif;font-weight:900;font-size:36px;letter-spacing:2px}
  .highlights .divider{width:2px;height:42px;background:var(--white)}
  .details{position:absolute;top:372px;left:40px;right:40px;text-align:center;font-size:19px;line-height:1.45}
  .details .sponsor{color:var(--blue);font-size:22px}
  .invite{position:absolute;top:450px;left:60px;right:60px;text-align:center;font-size:14px}
  .contacts{position:absolute;top:500px;left:40px;right:40px;display:flex;justify-content:space-between}
  .contact-col{display:flex;flex-direction:column;gap:10px}
  .contact{display:flex;font-size:16px}
  .contact .name{background:var(--green);color:var(--navy);padding:4px 12px;width:165px}
  .contact .phone{background:var(--blue);color:var(--white);padding:4px 12px;width:175px}
  .donation-note{position:absolute;top:612px;left:40px;right:40px;text-align:center;font-size:15px;line-height:1.45}
  .partners{position:absolute;top:680px;left:0;width:100%;display:flex;justify-content:center;gap:90px;align-items:center}
  .partner{font-family:"Open Sans",sans-serif;font-weight:600;font-size:28px;color:var(--navy)}
  .photo{position:absolute;left:0;top:760px;width:100%;height:260px;background:linear-gradient(180deg,rgba(255,255,255,1) 0%,rgba(196,170,150,.75) 35%,rgba(120,95,80,.8) 70%,rgba(2,85,163,.9) 100%)}
  .footer{position:absolute;left:0;bottom:0;width:100%;height:120px;background:var(--blue);color:var(--white);display:flex;align-items:center;padding:0 40px;gap:24px;font-family:"Montserrat",sans-serif;font-weight:800}
  .icon-box{width:62px;height:62px;border:2px solid var(--white);display:flex;align-items:center;justify-content:center;flex:none}
  .address{font-size:19px;line-height:1.35}
  .social{margin-left:auto;display:flex;align-items:center;gap:14px;font-size:17px}
  .social-square{width:40px;height:40px;border:2px solid var(--white)}
</style>
</head>
<body>
<main class="flyer">
  <header class="brand">
    <div class="brand-name">Glow<span class="accent">Run</span></div>
  </header>

  <div class="date-bar">
    <span><span class="label">Date:</span> 20 sep. 2020</span>
    <span class="divider"></span>
    <span><span class="label">Time:</span> 12pm-6pm</span>
  </div>

  <div class="annual-band"><h1>10TH ANNUAL PROGRAMME</h1></div>

  <div class="highlights">
    <span>FOOD</span><span class="divider"></span>
    <span>DRINKS</span><span class="divider"></span>
    <span>MUSIC+FUN</span>
  </div>

  <p class="details">Kids Games, Bounce House, Face Painting, Silent &amp; Live Auction, Bake Sale,<br>Raffles Children's Special by <span class="sponsor">HALVORSEN</span> 12-2 Walk in appts.</p>

  <p class="invite">If anyone wishes to donate any items or purchase a ticket, please contact one of the following people:</p>

  <section class="contacts">
    <div class="contact-col">
      <div class="contact"><span class="name">Megan Toll</span><span class="phone">(555)201-3348</span></div>
      <div class="contact"><span class="name">Dana Pruitt</span><span class="phone">(555)402-7719</span></div>
    </div>
    <div class="contact-col">
      <div class="contact"><span class="name">Kara Whitfield</span><span class="phone">(555)310-5521</span></div>
      <div class="contact"><span class="name">Beth Lorne</span><span class="phone">(555)310-6634</span></div>
    </div>
  </section>

  <p class="donation-note">All product donated to Riverbend Children's Hospital Northgate University RQ Center<br>to help find a cure! Sponsored by Family &amp; Friends of G.L.O.W.</p>

  <div class="partners">
    <span class="partner">RQ CENTER</span>
    <span class="partner">Riverbend</span>
  </div>

  <div class="photo" role="img" aria-label="Photo of children watching a live band at an outdoor event"></div>

  <footer class="footer">
    <div class="icon-box">
      <svg width="26" height="34" viewBox="0 0 26 34" aria-hidden="true">
        <path d="M13 1C6.4 1 1 6.2 1 12.6 1 21 13 33 13 33s12-12 12-20.4C25 6.2 19.6 1 13 1z" fill="#fff"/>
        <circle cx="13" cy="12.5" r="4.5" fill="#0255a3"/>
      </svg>
    </div>
    <div class="address">Maple County Fair Grounds<br>512 W. Orchard Rd., Fairview, IL 62400</div>
    <div class="social"><span class="social-square"></span><span>GlowRun Fundraiser</span></div>
  </footer>
</main>
</body>
</html>
```